Telmoro Business Card

I already have the conplay logo. I need to develop a professional business card layout

Target Market(s)

Business

Industry/Entity Type

Business

Contact Information for Business Card

Company Name: Telmoro Limited

Font styles to use
Sans Serif

Colors

Designer to choose colors to be used in the design.

Requirements
Must have
• Use current logo
• Need two card size options:
• Small Card: 70mm x 28mm (Landscape)
• Square Card: 65mm x 65mm
Nice to have
• I will need 8-10 files for each name, number and email address (details to follow)

```html
<!DOCTYPE html>
<html lang="en">
<head>
<meta charset="utf-8">
<title>Telmoro Business Card</title>
<link rel="stylesheet" href="https://fonts.googleapis.com/css2?family=Roboto+Condensed:wght@400;700&display=swap">
<style>
  :root {
    --backdrop: #e4e5e7;
    --card: #ffffff;
    --ink: #23217f;
    --brand: #27a8e0;
  }
  html, body {
    margin: 0;
    width: 1200px;
    height: 1000px;
    overflow: hidden;
    background: var(--backdrop);
    font-family: "Roboto Condensed", "Arial Narrow", sans-serif;
  }
  .card {
    position: absolute;
    left: 322px;
    top: 200px;
    width: 554px;
    height: 554px;
    border-radius: 60px;
    background: var(--card);
    overflow: hidden;
    color: var(--ink);
  }
  .wordmark {
    position: absolute;
    left: 58px;
    top: 70px;
    margin: 0;
    font-size: 76px;
    font-weight: 700;
    line-height: 1;
    letter-spacing: 1px;
    color: var(--brand);
  }
  .person {
    position: absolute;
    left: 61px;
    top: 180px;
  }
  .person-name {
    margin: 0;
    font-size: 25px;
    font-weight: 400;
    line-height: 30px;
  }
  .person-role {
    margin: 0;
    font-size: 16px;
    line-height: 20px;
  }
  .contact {
    position: absolute;
    left: 61px;
    top: 284px;
    margin: 0;
    font-style: normal;
    font-size: 20px;
    line-height: 26.5px;
  }
  .contact p { margin: 0; }
  .contact .company { margin-top: 26.5px; }
  .brand-band {
    position: absolute;
    left: 0;
    top: 462px;
    width: 554px;
    height: 92px;
    overflow: hidden;
  }
  .brand-band-text {
    position: absolute;
    left: 28px;
    top: -22px;
    margin: 0;
    font-size: 180px;
    font-weight: 700;
    line-height: 1;
    letter-spacing: 8px;
    color: var(--brand);
    white-space: nowrap;
  }
</style>
</head>
<body>
  <main class="card">
    <p class="wordmark">TELMORO</p>
    <div class="person">
      <h1 class="person-name">Clara Menton</h1>
      <p class="person-role">CEO</p>
    </div>
    <address class="contact">
      <p>0412 558 907</p>
      <p>clara@telmoro.com</p>
      <p class="company">Telmoro Limited</p>
      <p>48 Harbour Rd Telmoro 6789</p>
      <p>www.telmoro.com</p>
    </address>
    <div class="brand-band" aria-hidden="true">
      <p class="brand-band-text">TELMO</p>
    </div>
  </main>
</body>
</html>
```